Travel Consultant Business Card

Hello.. New travel consultant looking seeking a business card that incorporates my new logo. I specialize in cruises but also want to imply land vacation. I am very open to any design and font concepts. I'm looking for a very upbeat modern design that reflects cruise and land vacations. Bright vibrant colors

Target Market(s)

Cruise and Land Vacationers

Industry/Entity Type

Travel Agent

Contact Information for Business Card

I am very open to any design and font concepts. I'm looking for a very upbeat modern design that reflects cruise and land vacations. Bright vibrant colors

Colors

Designer to choose colors to be used in the design.

Requirements
Must have
• Company Name: MapleRidge Journeys---New logo uploaded to be included in design
• My Name: Dolores Kwiatek-Travel Consultant
• Phone Number: (555) 418-7093
• E-Mail Address: mapleridgejourneys@examplemail.net
• Website: www.mapleridgejourneys.example
Nice to have
• My tag line is …..Here to Get You There

```html
<!DOCTYPE html>
<html lang="en">
<head>
<meta charset="utf-8">
<title>MapleRidge Journeys – Business Card</title>
<link rel="stylesheet" href="https://fonts.googleapis.com/css2?family=Montserrat:wght@800&family=Poppins:wght@400&display=swap">
<style>
  :root {
    --stage: #1e2126;
    --royal: #1a5fb4;
    --royal-deep: #1652a0;
    --sky: #2aa7e6;
    --white: #ffffff;
    --grey: #5b6470;
  }
  * { margin: 0; padding: 0; box-sizing: border-box; }
  html, body { width: 1200px; height: 738px; overflow: hidden; }
  body {
    background: var(--stage);
    font-family: "Poppins", Arial, sans-serif;
    position: relative;
  }
  .card {
    position: absolute;
    top: 220px;
    width: 520px;
    height: 298px;
    overflow: hidden;
    box-shadow: 0 14px 30px rgba(0,0,0,.45);
  }
  .card--back { left: 50px; background: var(--royal); }
  .card--front { left: 630px; background: var(--white); }

  .brand {
    position: absolute;
    display: flex;
    align-items: center;
    gap: 10px;
    font-family: "Montserrat", Arial, sans-serif;
    font-weight: 800;
    font-size: 26px;
    letter-spacing: .5px;
    white-space: nowrap;
  }
  .brand__dot { width: 14px; height: 14px; border-radius: 50%; flex: none; }
  .card--back .brand { left: 50%; top: 50%; transform: translate(-50%, -50%); color: var(--white); }
  .card--back .brand__dot { background: var(--sky); }
  .card--front .brand { left: 30px; top: 88px; color: var(--royal); font-size: 22px; gap: 8px; }
  .card--front .brand__dot { width: 12px; height: 12px; background: var(--royal); }

  .holder { position: absolute; right: 26px; top: 20px; text-align: right; }
  .holder__name {
    font-family: "Montserrat", Arial, sans-serif;
    font-weight: 800; font-size: 17px; color: var(--royal-deep);
    text-transform: uppercase; letter-spacing: .3px;
  }
  .holder__role { font-size: 11px; color: var(--grey); margin-top: 1px; }

  .wave { position: absolute; inset: 0; width: 520px; height: 298px; }

  .contact {
    position: absolute; right: 22px; top: 150px;
    list-style: none; text-align: right;
    color: var(--white); font-size: 11.5px; line-height: 18px;
    white-space: nowrap;
  }
  .contact li { display: flex; justify-content: flex-end; align-items: center; gap: 6px; }
  .contact svg { width: 10px; height: 10px; flex: none; }
  .contact .no-icon { padding-right: 16px; }
</style>
</head>
<body>

  <section class="card card--back" aria-label="Card back">
    <div class="brand"><span class="brand__dot"></span>MapleRidge Journeys</div>
  </section>

  <section class="card card--front" aria-label="Card front">
    <svg class="wave" viewBox="0 0 520 298" aria-hidden="true">
      <defs>
        <path id="swell" d="M0,258 C110,292 190,262 250,200 C320,128 420,104 520,96 L520,340 L0,340 Z"/>
      </defs>
      <use href="#swell" transform="translate(0,-26)" fill="var(--royal)"/>
      <use href="#swell" transform="translate(0,-21)" fill="var(--white)"/>
      <use href="#swell" transform="translate(0,-16)" fill="var(--sky)"/>
      <use href="#swell" transform="translate(0,-7)" fill="var(--white)"/>
      <use href="#swell" fill="var(--royal)"/>
    </svg>

    <div class="holder">
      <div class="holder__name">Dolores Kwiatek</div>
      <div class="holder__role">Travel Consultant</div>
    </div>

    <div class="brand"><span class="brand__dot"></span>MapleRidge Journeys</div>

    <ul class="contact">
      <li class="no-icon">27 Harbourline Road,</li>
      <li class="no-icon">Port Avalen, NZ, 4620</li>
      <li>(555) 418-7093
        <svg viewBox="0 0 24 24"><path fill="currentColor" d="M6.6 10.8a15 15 0 0 0 6.6 6.6l2.2-2.2a1 1 0 0 1 1-.25 11.4 11.4 0 0 0 3.6.57 1 1 0 0 1 1 1V20a1 1 0 0 1-1 1A17 17 0 0 1 3 4a1 1 0 0 1 1-1h3.5a1 1 0 0 1 1 1c0 1.25.2 2.45.57 3.57a1 1 0 0 1-.25 1z"/></svg>
      </li>
      <li>mapleridgejourneys@examplemail.net
        <svg viewBox="0 0 24 24"><rect x="2" y="5" width="20" height="14" rx="2" fill="none" stroke="currentColor" stroke-width="2.4"/><path d="M3 6l9 7 9-7" fill="none" stroke="currentColor" stroke-width="2.4"/></svg>
      </li>
      <li>www.mapleridgejourneys.example
        <svg viewBox="0 0 24 24"><circle cx="12" cy="12" r="9.5" fill="none" stroke="currentColor" stroke-width="2.2"/><path d="M2.5 12h19M12 2.5c3 3 3 16 0 19M12 2.5c-3 3-3 16 0 19" fill="none" stroke="currentColor" stroke-width="1.8"/></svg>
      </li>
    </ul>
  </section>

</body>
</html>
```